Vegetable Grower Expo Backdrop

I need an 8x8 backdrop for an expo booth. We are a vegetable grower and have very limited graphics to work with. I have uploaded our logo which may not be the correct format and need to be updated for quality to print at that size. Need something quick and simple. Expo is August 18th

Target Market(s)

Retail and Wholesale buyers

Industry/Entity Type

Produce

Colors

Designer to choose colors to be used in the design.

Requirements
Must have
• Logo
Nice to have
• I am open to ideas!
Should not have
• Keep it simple and bottom 1/4 will be covered with samples so focus on top 3/4 of banner

```html
<!DOCTYPE html>
<html lang="en">
<head>
<meta charset="utf-8">
<title>Vegetable Grower Expo Backdrop</title>
<link rel="stylesheet" href="https://fonts.googleapis.com/css2?family=Bebas+Neue&family=Fraunces:opsz,wght@9..144,500;9..144,800&display=swap">
<style>
  :root {
    --page: #d9d9d9;
    --green-deep: #1f6b2e;
    --green: #2f8a3a;
    --green-bright: #7cb83a;
    --pill-dark: #2b7a34;
    --pill-light: #8ab43f;
    --paper: #f2f2ef;
    --white: #ffffff;
    --yellow: #f3eb2d;
  }
  * { margin: 0; padding: 0; box-sizing: border-box; }
  html, body { width: 720px; height: 1200px; overflow: hidden; background: var(--page); }
  .backdrop {
    position: absolute; left: 0; top: 240px; width: 720px; height: 720px;
    background: var(--paper); overflow: hidden;
  }
  .backdrop__field { position: absolute; inset: 0; width: 720px; height: 720px; }
  .brand {
    position: absolute; left: 34px; top: 104px; width: 166px;
    display: flex; align-items: center; gap: 10px;
    color: var(--white);
    font-family: "Fraunces", serif; font-weight: 800; font-size: 21px; line-height: 1.1;
  }
  .brand__mark {
    flex: none; width: 22px; height: 22px; border-radius: 50%;
    border: 3px solid var(--white);
  }
  .headline {
    position: absolute; left: 226px; top: 40px;
    font-family: "Bebas Neue", sans-serif; font-weight: 400; line-height: 0.86;
    transform: scaleX(0.82); transform-origin: left top;
    white-space: nowrap;
  }
  .headline__line { display: block; font-size: 93px; letter-spacing: 0.5px; }
  .headline__line--white { color: var(--white); }
  .headline__line--yellow { color: var(--yellow); }
  .event-date {
    position: absolute; left: 224px; top: 200px;
    font-family: "Fraunces", serif; font-weight: 800; font-size: 33px; line-height: 1;
    color: var(--white); letter-spacing: 0.3px;
  }
  .event-date sup { font-size: 17px; font-weight: 500; vertical-align: 15px; margin-left: 2px; }
  .produce-photo {
    position: absolute; left: 290px; top: 150px; width: 430px; height: 460px;
    background: radial-gradient(ellipse 55% 52% at 62% 56%, #c2402b 0%, #a8622c 30%, #6f8f2e 58%, rgba(124,184,58,0) 100%);
  }
  .features { position: absolute; left: 43px; top: 391px; width: 247px; list-style: none; }
  .feature {
    display: flex; align-items: center; height: 54px; margin-bottom: 5px;
    border-radius: 20px; padding-left: 12px; color: var(--white);
    font-family: "Fraunces", serif; font-weight: 500; font-size: 14.5px; line-height: 1.15;
  }
  .feature--dark { background: var(--pill-dark); }
  .feature--light { background: var(--pill-light); }
  .feature__icon { flex: none; width: 38px; height: 38px; margin-right: 13px; }
</style>
</head>
<body>
<main class="backdrop">
  <svg class="backdrop__field" viewBox="0 0 720 720" aria-hidden="true">
    <defs>
      <radialGradient id="rays" cx="0.72" cy="0.55" r="0.8">
        <stop offset="0" stop-color="#8cc63f"/>
        <stop offset="0.45" stop-color="#3f9a3c"/>
        <stop offset="1" stop-color="#1f6b2e"/>
      </radialGradient>
    </defs>
    <path fill="url(#rays)" d="M0 0H720V600H420L400 372 380 355 360 362 340 346 322 358 306 338 290 350 276 328 262 345 248 322 232 350 214 362 196 376 180 388 164 396 150 388 130 410 112 402 94 420 70 412 48 424 26 414 0 420Z"/>
  </svg>

  <div class="brand">
    <span class="brand__mark"></span>
    <span class="brand__name">Valley Ridge Growers</span>
  </div>

  <h1 class="headline">
    <span class="headline__line headline__line--white">Vegetable</span>
    <span class="headline__line headline__line--yellow">Grower Expo</span>
  </h1>
  <p class="event-date">AUGUST 18<sup>th</sup></p>

  <div class="produce-photo" role="img" aria-label="Wicker basket overflowing with peppers, red cabbage, carrots, broccoli, lettuce, tomatoes and onions"></div>

  <ul class="features">
    <li class="feature feature--dark">
      <svg class="feature__icon" viewBox="0 0 36 36" aria-hidden="true"><circle cx="18" cy="18" r="15" fill="none" stroke="#fff" stroke-width="1.6"/><path d="M18 26V13M18 17c-4-1-6-4-6-7 4 0 6 3 6 7Zm0 0c4-1 6-4 6-7-4 0-6 3-6 7Z" fill="none" stroke="#fff" stroke-width="1.6"/></svg>
      <span>Fresh Organic &amp;<br>Hybrid Vegetables</span>
    </li>
    <li class="feature feature--light">
      <svg class="feature__icon" viewBox="0 0 36 36" aria-hidden="true"><circle cx="18" cy="18" r="15" fill="none" stroke="#fff" stroke-width="1.6"/><path d="M11 24h14M13 24v-4M18 24v-7M23 24v-10M21 13l2-3 2 3" fill="none" stroke="#fff" stroke-width="1.6"/></svg>
      <span>Farm-to-Table<br>Success Stories</span>
    </li>
    <li class="feature feature--dark">
      <svg class="feature__icon" viewBox="0 0 36 36" aria-hidden="true"><circle cx="18" cy="18" r="15" fill="none" stroke="#fff" stroke-width="1.6"/><path d="M8 22c5-3 15-3 20 0M9 26c5-3 13-3 18 0M18 19v-8M18 14c-3 0-4-2-4-4 3 0 4 2 4 4Zm0 0c3 0 4-2 4-4-3 0-4 2-4 4Z" fill="none" stroke="#fff" stroke-width="1.6"/></svg>
      <span>Sustainable<br>Farming &amp; Agri-Tech</span>
    </li>
  </ul>
</main>
</body>
</html>
```